Larch Tutoring needs a flyer design

We are a tutoring company based in Melbourne. We provide group tutoring, private tutoring and workshop for VCE students. We are now seeking a flyer for our Study Sprint Sessions. We would like to see a neat and simple design contains essential information. Also the design should be targeting high school students and their parents. It should be eye-catching. Our tutors are 99.95 graduates(highest score achievers). This is also our strength.

Hi,

Thanks for showing interest.
The essential information should be time, location, and some details.

Time: 30/8, 6/9, 13/9, 20/9
Details: On every date, there are three groups, each contains 5 students and 1 tutors, for every subject. 10am-12, 12-2pm, 2-4pm are the session time for students to choose. Subjects are Chemistry, Maths Methods, Specialist Maths, Business Management, Further Maths and Biology.

Location is Harwick Reading Hall.(517 Pellinor Rd, Melbourne)

Our strength is that the tutors are 99.95 graduates, like full-marks obtainers. Notes are well designed by them to focus on BRQT exams.

Logo is on our web.

Contact detail: www.larchtutoring.example.au
contact@larchtutoring.example.au
www.facebook/larchtutoring

Measurement should be B4 size.

The essential information should be time, location, and some details. Time: 30/8, 6/9, 13/9, 20/9 Details: On every date, there are three groups, each contains 5 students and 1 tutors, for every subject. 10am-12, 12-2pm, 2-4pm are the session time for students to choose. Subjects are Chemistry, Maths Methods, Specialist Maths, Business Management, Further Maths and Biology. Location is Harwick Reading Hall.(517 Pellinor Rd, Melbourne) Our strength is that the tutors are 99.95 graduates, like full-marks obtainers. Notes are well designed by them to focus on BRQT exams. Logo is on our web. Contact detail: www.larchtutoring.example.au contact@larchtutoring.example.au www.facebook/larchtutoring Measurement should be B4 size. Cheers, Perrin

Target Market(s)

High school students and their parents

Industry/Entity Type

High School

Requirements
Must have
• Time: 30/8, 6/9, 13/9, 20/9

Logo is on our web.

Nice to have
• Eye-catching top lines.

```html
<!DOCTYPE html>
<html lang="en">
<head>
<meta charset="utf-8">
<title>Larch Tutoring – Study Sprint Sessions Flyer</title>
<link rel="stylesheet" href="https://fonts.googleapis.com/css2?family=PT+Sans+Narrow:wght@400;700&display=swap">
<style>
  :root {
    --backdrop: #1c1c1c;
    --ink: #2a1a10;
    --red: #ee3a1c;
    --yellow: #f3ef4c;
    --green: #3ee000;
    --white: #ffffff;
    --contact-yellow: #f7f25a;
  }
  * { margin: 0; padding: 0; box-sizing: border-box; }
  html, body { width: 1200px; height: 1000px; overflow: hidden; background: var(--backdrop); }
  body { position: relative; font-family: "PT Sans Narrow", "Arial Narrow", sans-serif; color: var(--ink); }

  .flyer { position: absolute; left: 275px; top: 73px; width: 622px; height: 880px; overflow: hidden; background: var(--white); }

  .hero-photo {
    position: absolute; inset: 0 0 80px 0;
    background:
      radial-gradient(ellipse 150px 210px at 150px 220px, #d9a98c 0%, rgba(217,169,140,0) 70%),
      radial-gradient(ellipse 200px 320px at 140px 460px, #5c7590 0%, rgba(92,117,144,0) 75%),
      radial-gradient(ellipse 160px 300px at 400px 330px, #c9d3dc 0%, rgba(201,211,220,0) 75%),
      linear-gradient(100deg, #3e6fb0 0%, #9ab4c8 18%, #c8d8a4 42%, #e9efe2 65%, #f6f8f6 88%, #ffffff 100%);
  }

  .bands { position: absolute; left: 0; top: 440px; width: 622px; height: 440px; }

  .brand { position: absolute; left: 330px; top: 120px; width: 260px; display: flex; align-items: center; justify-content: center; gap: 10px; }
  .brand-dot { width: 22px; height: 22px; border-radius: 50%; background: var(--red); }
  .brand-name { font-size: 34px; font-weight: 700; color: var(--red); }

  .strength { position: absolute; left: 300px; top: 178px; width: 270px; text-align: center; font-size: 24px; line-height: 34px; }
  .strength .highlight { color: var(--red); font-weight: 700; font-size: 33px; }

  .notes { position: absolute; left: 370px; top: 330px; width: 170px; font-size: 23px; line-height: 24px; }
  .notes .lead { font-size: 15px; line-height: 18px; display: block; }

  .clock { position: absolute; left: 270px; top: 420px; width: 104px; height: 104px; }

  .schedule { position: absolute; left: 0; top: 528px; width: 622px; text-align: center; }
  .schedule .time { font-size: 35px; line-height: 44px; }
  .schedule .details { font-size: 17.5px; line-height: 27px; margin-top: 6px; }
  .schedule strong { font-weight: 700; }

  .pin { position: absolute; left: 30px; top: 680px; width: 50px; height: 66px; }

  .location { position: absolute; left: 0; top: 748px; width: 622px; text-align: center; color: var(--white); font-size: 26px; }
  .location small { font-size: 18px; }

  .contact { position: absolute; left: 0; top: 802px; width: 622px; text-align: center; }
  .contact .lines { font-size: 17px; color: var(--contact-yellow); word-spacing: 2px; }
  .contact .lines span + span { margin-left: 18px; }
  .contact .site { font-size: 27px; color: var(--white); line-height: 32px; }
</style>
</head>
<body>
  <main class="flyer">
    <div class="hero-photo" role="img" aria-label="Photo of a smiling student with a backpack standing by a school doorway, classmates blurred behind"></div>

    <svg class="bands" viewBox="0 0 622 440" aria-hidden="true">
      <path d="M0 60 C160 10 420 10 622 55 L622 320 L0 320 Z" fill="var(--yellow)" opacity="0.85"/>
      <path d="M0 280 C180 320 420 300 622 272 L622 350 L0 350 Z" fill="var(--red)"/>
      <rect x="0" y="350" width="622" height="90" fill="var(--green)"/>
    </svg>

    <div class="brand">
      <span class="brand-dot"></span>
      <span class="brand-name">Larch Tutoring</span>
    </div>

    <p class="strength">Our strength is that the tutors<br>are <span class="highlight">99.95 graduates</span><br>like full-marks obtainers.</p>

    <p class="notes"><span class="lead">Notes are well designed by</span>them to focus on<br>BRQT exams.</p>

    <svg class="clock" viewBox="0 0 104 104" aria-hidden="true">
      <rect x="46" y="2" width="12" height="10" fill="var(--red)"/>
      <circle cx="52" cy="52" r="36" fill="var(--white)" stroke="var(--red)" stroke-width="9"/>
      <path d="M24 84 L16 96 M80 84 L88 96" stroke="var(--red)" stroke-width="8" stroke-linecap="round"/>
      <path d="M58 38 L44 52 L58 66" fill="none" stroke="var(--red)" stroke-width="7" stroke-linecap="round" stroke-linejoin="round"/>
    </svg>

    <section class="schedule">
      <p class="time">Time: 30/8, 6/9, 13/9, 20/9</p>
      <p class="details">
        <strong>Details:</strong> On every date, there are three groups,<br>
        each contains 5 students and 1 tutors, for every subject.<br>
        10am-12, 12-2pm, 2-4pm are the session time for students to choose.<br>
        <strong>Subjects are Chemistry, Maths Methods, Specialist Maths,<br>Business Management, Further Maths and Biology.</strong>
      </p>
    </section>

    <svg class="pin" viewBox="0 0 50 66" aria-hidden="true">
      <path d="M25 64 C10 44 2 34 2 24 A23 23 0 0 1 48 24 C48 34 40 44 25 64 Z" fill="var(--red)" stroke="var(--white)" stroke-width="2"/>
      <path d="M25 12 L28 21 L37 21 L30 27 L33 36 L25 30 L17 36 L20 27 L13 21 L22 21 Z" fill="var(--white)"/>
    </svg>

    <p class="location">Location is Harwick Reading Hall. <small>(517 Pellinor Rd, Melbourne)</small></p>

    <footer class="contact">
      <p class="lines"><span>contact@larchtutoring.example.au</span><span>www.facebook/larchtutoring</span></p>
      <p class="site">www.larchtutoring.example.au</p>
    </footer>
  </main>
</body>
</html>
```